Restyle corporate identity (+ logo) for a road construction company

We need a new logo and stationary design for our company VORMAX path. VORMAX path® increases the road base strength, while reducing major costs and time of road construction. Attached some examples of the current design.

Our wishes for the new logo:
- Business look
- Style sheet
- Modern

More information: www.vormaxpath-example.com
Updates

Target Market(s)

Government

Industry/Entity Type

Construction

Requirements
Must have
• Logo (with road sign) + text

```html
<!DOCTYPE html>
<html lang="en">
<head>
<meta charset="utf-8">
<title>VORMAX path — Business Card</title>
<link rel="stylesheet" href="https://fonts.googleapis.com/css2?family=Source+Sans+3:wght@400;600;700&display=swap">
<style>
  :root {
    --backdrop: #8f8f8f;
    --paper: #f1f1f0;
    --brand-green: #7ea31f;
    --brand-green-deep: #6f8c1c;
    --ink-grey: #8a8a8a;
    --ink-dark: #4a4a4a;
    --white: #ffffff;
  }
  * { box-sizing: border-box; margin: 0; padding: 0; }
  html, body {
    width: 1105px; height: 1200px; overflow: hidden;
    background: var(--backdrop);
    font-family: "Source Sans 3", "Segoe UI", sans-serif;
  }
  .canvas { position: relative; width: 1105px; height: 1200px; }

  .card {
    position: absolute; left: 182px; width: 747px; height: 427px;
  }
  .card--front { top: 119px; background: var(--paper); }
  .card--back  { top: 637px; background: var(--brand-green-deep); }

  .wordmark {
    position: absolute; display: flex; align-items: center; gap: 14px;
    font-weight: 600; font-size: 50px; letter-spacing: 1px; line-height: 1;
    white-space: nowrap;
  }
  .wordmark__square { width: 34px; height: 34px; flex: none; }
  .card--front .wordmark { right: 55px; top: 88px; color: var(--brand-green); }
  .card--front .wordmark__square { background: var(--brand-green); }
  .card--back .wordmark {
    left: 0; right: 0; top: 186px; justify-content: center; color: var(--white);
  }
  .card--back .wordmark__square { background: var(--white); }

  .accent-bar {
    position: absolute; left: 0; top: 219px; width: 15px; height: 55px;
    background: var(--brand-green);
  }
  .person { position: absolute; left: 52px; top: 219px; }
  .person__name {
    font-weight: 700; font-size: 25px; color: var(--brand-green);
    letter-spacing: 0.5px; line-height: 30px;
  }
  .person__role { font-size: 20px; color: var(--ink-grey); line-height: 26px; }

  .divider {
    position: absolute; left: 52px; right: 46px; top: 287px;
    height: 1.5px; background: var(--brand-green);
  }

  .contact-list, .address {
    position: absolute; top: 301px; list-style: none;
    font-size: 19.5px; color: var(--ink-dark); line-height: 29px;
  }
  .contact-list { left: 54px; }
  .contact-list li { display: flex; align-items: center; gap: 9px; }
  .contact-list svg { width: 17px; height: 17px; fill: var(--brand-green); flex: none; }
  .address { right: 46px; text-align: right; font-style: normal; }

  .card__url {
    position: absolute; left: 0; right: 0; top: 357px; text-align: center;
    color: var(--white); font-size: 18px; letter-spacing: 4px;
  }
</style>
</head>
<body>
<main class="canvas">
  <section class="card card--front" aria-label="Business card front">
    <div class="wordmark"><span class="wordmark__square"></span>VORMAX path</div>
    <span class="accent-bar"></span>
    <div class="person">
      <p class="person__name">DANIEL VERHOEF</p>
      <p class="person__role">CEO/Founder</p>
    </div>
    <span class="divider"></span>
    <ul class="contact-list">
      <li>
        <svg viewBox="0 0 24 24" aria-hidden="true"><path d="M6.6 10.8a15.1 15.1 0 0 0 6.6 6.6l2.2-2.2c.3-.3.7-.4 1-.2 1.1.4 2.3.6 3.6.6.6 0 1 .4 1 1V20c0 .6-.4 1-1 1A17 17 0 0 1 3 4c0-.6.4-1 1-1h3.5c.6 0 1 .4 1 1 0 1.3.2 2.5.6 3.6.1.3 0 .7-.2 1z"/></svg>
        612 555 0148
      </li>
      <li>
        <svg viewBox="0 0 24 24" aria-hidden="true"><path d="M2 5h20v14H2z M3.5 6.5 12 12.5l8.5-6" stroke="var(--paper)" stroke-width="1.6"/></svg>
        contact@vormaxpath-example.com
      </li>
      <li>
        <svg viewBox="0 0 24 24" aria-hidden="true"><circle cx="12" cy="12" r="10"/><path d="M7 6c2 1 3 3 2 5s1 3 2 5M15 5c-1 2 1 3 3 4M14 14c1 1 2 3 1 5" stroke="var(--paper)" stroke-width="1.6" fill="none"/></svg>
        www.vormaxpath-example.com
      </li>
    </ul>
    <address class="address">
      Lindenlaan 27<br>
      2583 KL The Hague<br>
      The Netherlands
    </address>
  </section>

  <section class="card card--back" aria-label="Business card back">
    <div class="wordmark"><span class="wordmark__square"></span>VORMAX path</div>
    <p class="card__url">www.vormaxpath-example.com</p>
  </section>
</main>
</body>
</html>
```